Harrowgate Supply Group Business Card Design

The Business Card will be one side only with Harrowgate Supplies Group Logo
Card should have:
Name
Title
Office phone Number
Cell Number
email address
Website
Street Address
Our Slogan is Rugged and Reliable
Looking for something that stands out from other business cards

Target Market(s)

Heavy equipment Lease Company

```html
<!DOCTYPE html>
<html lang="en">
<head>
<meta charset="utf-8">
<title>Harrowgate Supplies Group – Business Card</title>
<link href="https://fonts.googleapis.com/css2?family=Montserrat:wght@500;700;800&family=Lato:wght@300;400;700&display=swap" rel="stylesheet">
<style>
  :root {
    --page-bg: #e6e4e0;
    --card-bg: #ffffff;
    --navy: #2f3178;
    --navy-light: #6a6aa8;
    --red: #d3203f;
    --red-light: #e0566e;
    --text-grey: #8a8a8a;
  }
  * { margin: 0; padding: 0; box-sizing: border-box; }
  html, body {
    width: 1200px; height: 950px; overflow: hidden;
    background: var(--page-bg);
  }
  .business-card {
    position: absolute; left: 100px; top: 189px;
    width: 1000px; height: 572px;
    background: var(--card-bg);
    box-shadow: 0 4px 18px rgba(0,0,0,0.12);
    overflow: hidden;
  }
  .emblem-area {
    position: absolute; left: 70px; top: 40px;
    width: 510px; height: 492px;
    background: linear-gradient(90deg, var(--navy-light) 0%, var(--navy) 70%, var(--red) 100%);
  }
  .holder {
    position: absolute; left: 325px; top: 272px;
    transform: translateX(-50%);
    text-align: center; color: #fff;
    font-family: "Montserrat", sans-serif;
    white-space: nowrap;
  }
  .holder-name { font-size: 30px; font-weight: 500; letter-spacing: 1px; }
  .holder-title { font-size: 19px; font-weight: 500; letter-spacing: 1px; margin-top: 2px; }
  .company-block {
    position: absolute; left: 610px; top: 52px; width: 370px;
  }
  .company-name {
    font-family: "Montserrat", sans-serif;
    font-weight: 800; color: var(--red);
    font-size: 26px; line-height: 1.15;
    letter-spacing: 0.5px;
  }
  .name-rule {
    height: 2px; width: 100%;
    background: var(--navy);
    margin-top: 12px;
  }
  .contact-details {
    margin-top: 26px;
    font-family: "Lato", sans-serif; font-weight: 300;
    color: var(--text-grey); font-size: 21px; line-height: 1.4;
  }
  .contact-details .gap { margin-top: 14px; }
  .contact-label { font-weight: 700; color: var(--navy); }
  .slogan {
    margin-top: 22px;
    font-family: "Montserrat", sans-serif; font-weight: 700;
    font-size: 28px; color: var(--navy); letter-spacing: 0.5px;
  }
  .slogan .accent { color: var(--red); }
</style>
</head>
<body>
  <section class="business-card">
    <div class="emblem-area" role="img" aria-label="Large navy star emblem with red stripes"></div>

    <div class="holder">
      <div class="holder-name">DANIEL MERCER</div>
      <div class="holder-title">CEO/FOUNDER</div>
    </div>

    <div class="company-block">
      <div class="company-name">HARROWGATE SUPPLIES GROUP</div>
      <div class="name-rule"></div>
      <div class="contact-details">
        <div>4120 Birchfield Road</div>
        <div>Fairbanks, Alaska 99701</div>
        <div class="gap"><span class="contact-label">PHONE:</span> 555 214 7730</div>
        <div><span class="contact-label">CELL:</span> 555 389 6152</div>
        <div class="gap">daniel@harrowgatesupplies.com</div>
        <div>harrowgatesupplies.com</div>
      </div>
      <div class="slogan">RUGGED &amp; <span class="accent">RELIABLE</span></div>
    </div>
  </section>
</body>
</html>
```